New look modernised front page for Pellmark Sporting League Website Which incorporates our new logo (to be provided as a png file)
We want the home page to a panel to allow an image rotator and provide ready access to links to other inflation via some link menus/panel/button
1. Join a Croquet Club - links to details about Croquet in NSW - gateway to information of interest or the general public/“interested others” eg about the game, clubs locations and contacts
2. Club and Member Information - newsletters, Calender of events, and downloads
3. Officials and volunteers - training resources etc
4. Member and Club sign in - access to database
5. About Us - information about Pellmark Sporting League incorporated -peak body for croquet in NSW - governance, contact details etc

Current website is at https://www.pellmark-league.org/index.html

Target Market(s)

Dual target - People interested in learning about croquet and existing members

Number of Pages Required

1 page

Font styles to use
Sans Serif

Colors
0255a3
3377b5
85acd3
85cae6
33a6d7
0792cd
00a990

Requirements
Must have
• Contemporary feel
• Include logo - file attached
• Colours to include blues which are the NSW colour
Nice to have
• We want the home page to a panel to allow an image rotator and provide ready access to links to other inflation via some link menus/panel/button
• 1. Join a Croquet Club - links to details about Croquet in NSW - gateway to information of interest or the general public/“interested others” eg about the game, clubs locations and contacts
• 2. Club and Member Information - newsletters, Calender of events, and downloads
• 3. Officials and volunteers - training resources etc
• 4. Member and Club sign in - access to database
• 5. About Us - information about Pellmark Sporting League incorporated -peak body for croquet in NSW - governance, contact details etc
• Want to have feeling of activity/movement/alive
• Current website is at https://www.pellmark-league.org/index.html
• Some photos attached for information

```html
<!DOCTYPE html>
<html lang="en">
<head>
<meta charset="utf-8">
<title>Pellmark Sporting League — Home</title>
<link rel="stylesheet" href="https://fonts.googleapis.com/css2?family=Oswald:wght@300;400;500&family=Open+Sans:wght@400;600;700&display=swap">
<style>
  :root {
    --navy: #0255a3;
    --blue-mid: #3377b5;
    --blue-soft: #85acd3;
    --sky: #85cae6;
    --azure: #33a6d7;
    --cyan: #0792cd;
    --green: #00a990;
    --ink: #3d4450;
    --ink-soft: #6b7280;
    --rule: #d7dde4;
    --white: #ffffff;
  }
  * { box-sizing: border-box; margin: 0; padding: 0; }
  html, body { width: 1200px; height: 900px; overflow: hidden; background: var(--white); }
  body { font-family: "Open Sans", Arial, sans-serif; color: var(--ink); }

  .site-header {
    height: 84px; display: flex; align-items: center; padding: 0 56px;
    background: var(--white); position: relative; z-index: 2;
  }
  .brand { display: flex; align-items: center; gap: 10px; }
  .brand-mark { width: 18px; height: 18px; background: var(--cyan); }
  .brand-name { font-family: "Oswald", sans-serif; font-weight: 500; font-size: 20px; color: var(--navy); letter-spacing: .3px; }

  .main-nav { margin-left: auto; display: flex; align-items: center; gap: 30px; }
  .nav-link {
    font-family: "Oswald", sans-serif; font-size: 11.5px; font-weight: 500;
    text-transform: uppercase; color: var(--ink); text-decoration: none; letter-spacing: .6px;
    position: relative;
  }
  .nav-link.is-active { color: var(--azure); }
  .nav-link.is-active::before {
    content: ""; position: absolute; left: -4px; right: -4px; top: -14px; height: 2px; background: var(--azure);
  }
  .nav-link.is-active::after {
    content: ""; position: absolute; left: 50%; bottom: -12px; width: 6px; height: 6px; margin-left: -3px;
    border: 1.5px solid var(--azure); border-radius: 50%;
  }
  .login-button {
    margin-left: 12px; display: flex; align-items: center; gap: 7px;
    background: var(--navy); color: var(--white); border-radius: 20px; padding: 9px 22px;
    font-family: "Oswald", sans-serif; font-size: 11.5px; font-weight: 500; letter-spacing: .6px;
    text-transform: uppercase; text-decoration: none;
  }

  .hero { position: relative; height: 540px; overflow: hidden; }
  .hero-photo {
    position: absolute; inset: 0;
    background: linear-gradient(180deg, #3b4a33 0%, #4f5a3e 38%, #6a6e52 60%, #4d5846 100%);
  }
  .hero-shade { position: absolute; inset: 0; background: rgba(20, 28, 24, .35); }
  .hero-copy { position: absolute; left: 0; right: 0; top: 210px; text-align: center; color: var(--white); }
  .hero-title {
    font-family: "Oswald", sans-serif; font-weight: 400; font-style: italic;
    font-size: 40px; line-height: 1.2; text-shadow: 0 2px 6px rgba(0,0,0,.35);
  }
  .hero-cta {
    display: inline-block; margin-top: 22px; position: relative;
    background: var(--azure); color: var(--white); border-radius: 20px; padding: 9px 26px;
    font-family: "Oswald", sans-serif; font-size: 11.5px; font-weight: 500; letter-spacing: .6px;
    text-transform: uppercase; text-decoration: none;
  }
  .hero-cta::after {
    content: ""; position: absolute; left: 50%; bottom: -12px; width: 6px; height: 6px; margin-left: -3px;
    background: var(--white); border-radius: 50%;
  }
  .slider-arrow {
    position: absolute; top: 256px; width: 34px; height: 34px; border-radius: 50%;
    background: rgba(255,255,255,.9); display: flex; align-items: center; justify-content: center;
  }
  .slider-arrow.prev { left: 40px; }
  .slider-arrow.next { right: 40px; }

  .results { padding-top: 34px; }
  .section-title {
    display: flex; align-items: flex-start; justify-content: center; gap: 24px;
    font-family: "Oswald", sans-serif; font-weight: 300; font-size: 32px; line-height: 44px; color: var(--ink);
  }
  .section-title .accent { color: var(--azure); font-weight: 400; }
  .title-rule { width: 210px; height: 14px; margin-top: 10px; border-top: 1.5px solid var(--azure); }
  .title-rule.left { border-left: 1.5px solid var(--azure); }
  .title-rule.right { border-right: 1.5px solid var(--azure); }

  .results-table { width: 760px; margin: 22px auto 0; border-collapse: collapse; font-size: 12px; }
  .results-table th {
    background: var(--azure); color: var(--white); text-align: left; font-weight: 500;
    font-family: "Oswald", sans-serif; font-size: 14px; font-style: italic; padding: 9px 18px;
    border-right: 1px solid rgba(255,255,255,.5);
  }
  .results-table th:last-child { border-right: none; clip-path: polygon(0 0, 100% 0, 96% 100%, 0 100%); }
  .results-table td { padding: 11px 18px; border-bottom: 1px solid var(--rule); border-right: 1px solid var(--rule); color: var(--ink-soft); }
  .results-table td:last-child { border-right: none; }
  .col-event { width: 46%; }
  .col-winner { width: 30%; }
</style>
</head>
<body>
  <header class="site-header">
    <div class="brand">
      <span class="brand-mark"></span>
      <span class="brand-name">Pellmark Sporting League</span>
    </div>
    <nav class="main-nav">
      <a class="nav-link is-active" href="#">Home</a>
      <a class="nav-link" href="#">About Us</a>
      <a class="nav-link" href="#">Why Choose Us</a>
      <a class="nav-link" href="#">Event</a>
      <a class="nav-link" href="#">Gallery</a>
      <a class="nav-link" href="#">Coaches</a>
      <a class="nav-link" href="#">Result</a>
      <a class="nav-link" href="#">Contact Us</a>
      <a class="login-button" href="#">
        <svg width="11" height="11" viewBox="0 0 12 12" aria-hidden="true"><circle cx="6" cy="3.5" r="2.5" fill="#fff"/><path d="M1 12c0-3 2.2-5 5-5s5 2 5 5z" fill="#fff"/></svg>
        Login / Register
      </a>
    </nav>
  </header>

  <section class="hero">
    <div class="hero-photo" role="img" aria-label="Croquet players dressed in white standing on a grass lawn holding mallets, with trees behind"></div>
    <div class="hero-shade"></div>
    <div class="hero-copy">
      <h1 class="hero-title">Croquet is a very old game<br>that had its beginnings in the early 1400's!</h1>
      <a class="hero-cta" href="#">Explore More</a>
    </div>
    <span class="slider-arrow prev"><svg width="10" height="12" viewBox="0 0 10 12" aria-hidden="true"><path d="M8 1 2 6l6 5z" fill="#3d4450"/></svg></span>
    <span class="slider-arrow next"><svg width="10" height="12" viewBox="0 0 10 12" aria-hidden="true"><path d="M2 1l6 5-6 5z" fill="#3d4450"/></svg></span>
  </section>

  <section class="results">
    <h2 class="section-title"><span class="title-rule left"></span><span>Latest <span class="accent">Results</span></span><span class="title-rule right"></span></h2>
    <table class="results-table">
      <thead>
        <tr><th class="col-event">Event</th><th class="col-winner">Winner</th><th>Runner-Up</th></tr>
      </thead>
      <tbody>
        <tr><td>Harbour Open Men's Singles Championship – X Event</td><td>Helen Marsh &amp; David Corrin</td><td>Graham Ellery</td></tr>
        <tr><td>Harbour Open Men's Singles Championship – Z Event</td><td>Owen Talbot</td><td>---</td></tr>
        <tr><td>Harbour Open Men's Singles Championship – Y Event</td><td>Peter Randle</td><td>---</td></tr>
      </tbody>
    </table>
  </section>
</body>
</html>
```